Sticker design

We did an instagram post a while back and would like a sticker with the quote on it. https://www.pictogramly.example/clip/Rb7Kt9pQvWd/?ref=Q2VxNDFtaGVwcTR6

We’d like the quote to be the audio.

We loved the shirts you did last week.

```html
<!DOCTYPE html>
<html lang="en">
<head>
<meta charset="utf-8">
<title>Glacier Water Quote Stickers</title>
<link href="https://fonts.googleapis.com/css2?family=Asap:wght@600&family=Oswald:wght@500&display=swap" rel="stylesheet">
<style>
  :root {
    --canvas: #ffffff;
    --navy: #1e2259;
    --royal: #1a4e86;
    --sky: #55afcf;
    --green: #3eb959;
    --ink: #ffffff;
  }
  * { margin: 0; padding: 0; box-sizing: border-box; }
  html, body {
    width: 1200px;
    height: 1200px;
    overflow: hidden;
    background: var(--canvas);
  }
  .sheet {
    position: relative;
    width: 1200px;
    height: 1200px;
  }
  .sticker {
    position: absolute;
  }
  .sticker--square-stitched {
    left: 124px; top: 100px;
    width: 424px; height: 422px;
    border-radius: 30px;
    background: var(--navy);
  }
  .sticker--square-stitched::after {
    content: "";
    position: absolute;
    inset: 10px;
    border: 1.5px dashed rgba(255,255,255,0.85);
    border-radius: 22px;
  }
  .sticker--circle-royal {
    left: 648px; top: 91px;
    width: 440px; height: 440px;
    border-radius: 50%;
    background: var(--royal);
  }
  .sticker--circle-sky {
    left: 98px; top: 612px;
    width: 478px; height: 478px;
    border-radius: 50%;
    background: var(--sky);
  }
  .sticker--square-framed {
    left: 664px; top: 640px;
    width: 423px; height: 423px;
    border-radius: 30px;
    background: var(--green);
  }
  .sticker--square-framed::after {
    content: "";
    position: absolute;
    inset: 12px;
    border: 1.5px solid rgba(255,255,255,0.9);
    border-radius: 22px;
  }
  .quote {
    position: absolute;
    left: 0; right: 0;
    text-align: center;
    color: var(--ink);
    white-space: nowrap;
  }
  .quote--sentence {
    font-family: "Asap", sans-serif;
    font-weight: 600;
  }
  .quote--caps {
    font-family: "Oswald", sans-serif;
    font-weight: 500;
    text-transform: uppercase;
  }
  .sticker--square-stitched .quote {
    top: 54px;
    font-size: 47px;
    line-height: 56px;
  }
  .sticker--circle-royal .quote {
    top: 77px;
    font-size: 44px;
    line-height: 51px;
  }
  .sticker--circle-sky .quote {
    top: 86px;
    font-size: 50px;
    line-height: 55px;
  }
  .sticker--square-framed .quote {
    top: 38px;
    font-size: 52px;
    line-height: 58px;
  }
</style>
</head>
<body>
  <main class="sheet">
    <div class="sticker sticker--square-stitched">
      <p class="quote quote--sentence">That's water<br>from a glacier<br>in Alaska.<br>It was blessed<br>by an Eskimo<br>medicine.</p>
    </div>
    <div class="sticker sticker--circle-royal">
      <p class="quote quote--sentence">That's water<br>from a glacier<br>in Alaska.<br>It was blessed<br>by an Eskimo<br>medicine.</p>
    </div>
    <div class="sticker sticker--circle-sky">
      <p class="quote quote--caps">That's water<br>from a glacier<br>in Alaska.<br>It was blessed<br>by an Eskimo<br>medicine.</p>
    </div>
    <div class="sticker sticker--square-framed">
      <p class="quote quote--caps">That's water<br>from a glacier<br>in Alaska.<br>It was blessed<br>by an Eskimo<br>medicine.</p>
    </div>
  </main>
</body>
</html>
```